Real Estate Investment Company Needs Business Card Design

TurnKeyDeal9 is a real estate investment company that primarily deals directly with homeowners looking to sell their homes in "as is" condition as quick as possible. We give this seller cash and close on their nightmare of a property in just a matter of days.

Our logo is attached - (please keep logo in tact, use as is)

Industry/Entity Type

Real Estate

Contact Information for Business Card

The design should invoke trust & professionalism. The person holding the card should feel rest assured that we are the right company to work with.

Font styles to use
Sans Serif

Requirements
Must have
• Card must include "Call us today for a fair offer on your property so you can move on with your life!"
Nice to have
• If possible, include this either on front or back (you can use your own formatting, below is just the text)
• "
• No Realtor Commissions
• No Repairs To Deal With
• No Closing Costs "

```html
<!DOCTYPE html>
<html lang="en">
<head>
<meta charset="utf-8">
<title>TurnKeyDeal9 Business Card</title>
<link href="https://fonts.googleapis.com/css2?family=Open+Sans:wght@600;700&family=Oswald:wght@400;500;600&display=swap" rel="stylesheet">
<style>
  :root {
    --page-bg: #e6e6e6;
    --card-white: #ffffff;
    --card-black: #121417;
    --card-black-edge: #23272c;
    --brand-blue: #3d87c9;
    --ink-dark: #1c1c1c;
    --ink-mid: #2b2b2b;
    --phone-red: #c4282b;
    --phone-red-dark: #8e1518;
  }
  * { box-sizing: border-box; margin: 0; padding: 0; }
  html, body {
    width: 1200px;
    height: 871px;
    overflow: hidden;
    background: var(--page-bg);
  }
  .sheet {
    position: relative;
    width: 1200px;
    height: 871px;
  }
  .card {
    position: absolute;
    left: 250px;
    width: 700px;
    height: 400px;
    border-radius: 4px;
    box-shadow: 0 4px 14px rgba(0,0,0,0.18);
    overflow: hidden;
  }
  /* Back side */
  .card--back {
    top: 24px;
    background: radial-gradient(ellipse at 50% 40%, var(--card-black-edge) 0%, var(--card-black) 70%);
    display: flex;
    align-items: center;
    justify-content: center;
  }
  .brand-name {
    font-family: "Open Sans", sans-serif;
    font-weight: 700;
    color: var(--brand-blue);
    letter-spacing: -0.5px;
    white-space: nowrap;
  }
  .card--back .brand-name { font-size: 62px; }
  .brand-dot {
    display: inline-block;
    width: 14px;
    height: 14px;
    border-radius: 50%;
    background: var(--brand-blue);
    margin-left: 8px;
    vertical-align: middle;
  }

  /* Front side */
  .card--front {
    top: 447px;
    background: var(--card-white);
  }
  .card--front .brand-name {
    position: absolute;
    left: 48px;
    top: 128px;
    font-size: 42px;
  }
  .offer {
    position: absolute;
    left: 40px;
    top: 250px;
    width: 290px;
    text-align: center;
    font-family: "Open Sans", sans-serif;
  }
  .offer__lead {
    color: var(--brand-blue);
    font-size: 14px;
    font-weight: 700;
  }
  .offer__text {
    color: var(--ink-dark);
    font-size: 11.5px;
    font-weight: 600;
    margin-top: 1px;
  }
  .offer__phone {
    color: var(--brand-blue);
    font-family: "Oswald", sans-serif;
    font-size: 20px;
    font-weight: 400;
    letter-spacing: 2px;
    margin-top: 2px;
  }
  .telephone-art {
    position: absolute;
    left: 330px;
    top: 278px;
    width: 72px;
    height: 58px;
    border-radius: 12px 12px 6px 6px;
    background: radial-gradient(ellipse at 45% 40%, var(--phone-red) 0%, var(--phone-red-dark) 100%);
  }
  .divider {
    position: absolute;
    left: 420px;
    top: 86px;
    width: 3px;
    height: 168px;
    background: var(--brand-blue);
  }
  .contact {
    position: absolute;
    left: 440px;
    top: 96px;
    font-family: "Oswald", sans-serif;
  }
  .contact__name {
    color: var(--ink-dark);
    font-size: 34px;
    font-weight: 600;
    letter-spacing: 1.5px;
    line-height: 1;
  }
  .contact__title {
    color: var(--brand-blue);
    font-size: 16px;
    font-weight: 600;
    letter-spacing: 2.5px;
    margin-top: 4px;
  }
  .contact__row {
    display: flex;
    align-items: center;
    gap: 8px;
    color: var(--ink-mid);
    font-size: 19px;
    font-weight: 500;
    letter-spacing: 2px;
    margin-top: 4px;
  }
  .contact__row svg { width: 15px; height: 15px; fill: var(--brand-blue); flex: none; }
  .benefits {
    position: absolute;
    left: 440px;
    top: 285px;
    list-style: none;
    font-family: "Oswald", sans-serif;
    color: var(--brand-blue);
    font-size: 21px;
    font-weight: 500;
    letter-spacing: 1.5px;
    line-height: 1.2;
  }
</style>
</head>
<body>
<main class="sheet">
  <section class="card card--back" aria-label="Card back">
    <span class="brand-name">TurnKeyDeal9<span class="brand-dot"></span></span>
  </section>

  <section class="card card--front" aria-label="Card front">
    <span class="brand-name">TurnKeyDeal9<span class="brand-dot"></span></span>

    <div class="offer">
      <p class="offer__lead">Call us today</p>
      <p class="offer__text">for a fair offer so you can move on with your life!</p>
      <p class="offer__phone">00-000-0000</p>
    </div>
    <div class="telephone-art" role="img" aria-label="Red rotary telephone"></div>

    <div class="divider"></div>
    <div class="contact">
      <p class="contact__name">Your Name</p>
      <p class="contact__title">JOB TITLE</p>
      <p class="contact__row">
        <svg viewBox="0 0 16 16" aria-hidden="true"><path d="M8 0a5.5 5.5 0 0 0-5.5 5.5C2.5 10 8 16 8 16s5.5-6 5.5-10.5A5.5 5.5 0 0 0 8 0zm0 8a2.5 2.5 0 1 1 0-5 2.5 2.5 0 0 1 0 5z"/></svg>
        Address
      </p>
      <p class="contact__row">
        <svg viewBox="0 0 16 16" aria-hidden="true"><path d="M1 5c0-2 3-3 7-3s7 1 7 3v1.5h-3.5V5h-7v1.5H1z"/><rect x="3" y="7.5" width="10" height="6" rx="1.5"/></svg>
        000-000-0000
      </p>
      <p class="contact__row">
        <svg viewBox="0 0 16 16" aria-hidden="true"><path d="M1 3h14v1.2L8 9 1 4.2z"/><path d="M1 6l7 4.8L15 6v7H1z"/></svg>
        Email@
      </p>
    </div>

    <ul class="benefits">
      <li>* No Realtor Commissions</li>
      <li>* No Repairs To Deal With</li>
      <li>* No Closing Cost</li>
    </ul>
  </section>
</main>
</body>
</html>
```